Dive Bar/ Pop Culture Bar Adult Nugget Night

Hey guys,
Lorne here from Rusty Gabs restaurant in Australia. Im after a poster design for our new Monday Night Special - Adult Nugget Night. - Think crumbed chicken or Beef Schnitzel with different toppings like Philly Cheese steak or Cheese burger smash (aka a parmy).

I'm thinking a plain block blue colour background with a vector image as the main focus - see attached graphics. I would like the poster to be a fun and tongue in cheek and a 80's/90's hip hop vibe and vector image of a nugget "thug life".

The info it has to contain are as follows -
- Adult Nugget Night (title)
- Monday Night
- Price $17
- from 5pm

Toppings
- Philly Cheese Steak
- Cheese burger Smash
- Burnt End Beanz

A little about Rusty Gabs
-Rusty Gabs came about because we fell in love with the old- skool American south culture of slow cooked soul food, thrown together on big hearty share plates in the backyard and tucked into with the ones you love.

We wanted to bring something different to the coast.

Moody and grungy without losing the soul of why we go out to drink and eat in the first place - to fill our bellies and warm our hearts.

That's why communal eating is at the core of what we do. Low 'n' Slow platters of scrumptious, fall off the bone meat. Sided with delicious dishes of your choice. That quietness that falls on the table as everyone savours the flavours. Laughs as you reach across your mate, to fork that last juicy piece of slow cooked meat that someone else was eyeing off. Washing it all down with hand-crafted beer, or better yet, that top shelf whiskey glistening from the back bar. Finishing off the night with the best kind of dessert.. our famous Sticky Date Espresso Martini!

I have found one image on the net that I like....... don't know if it's useful...

Please reach out for any more info or questions needed

Cheers
Lorne

Target Market(s)

20-40 year old for a funky grudge bar

Industry/Entity Type

Dive Bar, Smokehouse, Bar & Grill

Font styles to use
Other font styles liked:
• Veneer

Colors
0054AA
0677BA
7BADD7
CADEEF
E8F1F8
FFF300
FFF600
FEFA6F
FFFEC7
FFFEE8
F0912C
F2A743
F7CA91
FBE8D2
FDF5EE
EB3D1F
EC4F4E
F09395
F8D3D4
FCEDEE

Requirements
Must have
• Business Name "Rusty Gabs" will share Logo in later stages
Nice to have
• Nice bold colours which throw back to 1980/90's pop culture

```html
<!DOCTYPE html>
<html lang="en">
<head>
<meta charset="utf-8">
<title>Adult Nugget Nights</title>
<link rel="stylesheet" href="https://fonts.googleapis.com/css2?family=Jost:wght@600&family=Quicksand:wght@400;500&display=swap">
<style>
  :root {
    --bg-centre: #a8dfe0;
    --bg-edge: #5cc1da;
    --ink: #0f1a1f;
    --bullet: #c4ece6;
    --nugget-light: #fbb04e;
    --nugget-dark: #ee7a2e;
    --floor: #0399c8;
  }
  html, body {
    margin: 0;
    padding: 0;
    overflow: hidden;
  }
  .poster {
    position: relative;
    width: 848px;
    height: 1200px;
    overflow: hidden;
    background: radial-gradient(ellipse 60% 55% at 45% 52%, var(--bg-centre) 0%, var(--bg-edge) 100%);
    color: var(--ink);
    font-family: "Quicksand", sans-serif;
  }
  .title {
    position: absolute;
    left: 68px;
    top: 52px;
    margin: 0;
    font-family: "Jost", sans-serif;
    font-weight: 600;
    font-size: 108px;
    line-height: 113px;
    letter-spacing: 6px;
    text-transform: uppercase;
  }
  .title span { display: block; }
  .mascot {
    position: absolute;
    left: 74px;
    top: 452px;
    width: 520px;
    height: 472px;
  }
  .details {
    position: absolute;
    left: 570px;
    top: 546px;
    font-size: 24px;
    line-height: 1;
  }
  .details p { margin: 0; }
  .details .day { margin-bottom: 16px; }
  .details .price-row {
    display: flex;
    align-items: center;
    gap: 24px;
    margin-bottom: 10px;
  }
  .details .amount {
    font-size: 48px;
    letter-spacing: -1px;
  }
  .toppings {
    position: absolute;
    left: 286px;
    top: 948px;
  }
  .toppings h2 {
    margin: 0 0 36px;
    font-weight: 400;
    font-size: 24px;
  }
  .toppings ul {
    list-style: none;
    margin: 0;
    padding: 0;
  }
  .toppings li {
    position: relative;
    padding-left: 21px;
    font-size: 25px;
    letter-spacing: 0.6px;
    line-height: 1;
    margin-bottom: 18px;
  }
  .toppings li::before {
    content: "";
    position: absolute;
    left: 0;
    bottom: 1px;
    width: 11px;
    height: 11px;
    background: var(--bullet);
  }
</style>
</head>
<body>
<main class="poster">
  <h1 class="title">
    <span>Adult</span>
    <span>Nugget</span>
    <span>Nights</span>
  </h1>

  <svg class="mascot" viewBox="0 0 520 472" role="img" aria-label="Illustration of a cartoon chicken nugget mascot in a red cap and sneakers, striking a hip hop pose on a blue floor shadow">
    <defs>
      <linearGradient id="mascot-fill" x1="0" y1="0" x2="1" y2="1">
        <stop offset="0" stop-color="var(--nugget-light)"/>
        <stop offset="1" stop-color="var(--nugget-dark)"/>
      </linearGradient>
    </defs>
    <ellipse cx="260" cy="432" rx="258" ry="32" fill="var(--floor)"/>
    <rect x="80" y="0" width="360" height="410" rx="40" fill="url(#mascot-fill)" opacity="0.85"/>
  </svg>

  <section class="details">
    <p class="day">Monday Night</p>
    <p class="price-row"><span>Price</span><span class="amount">$17</span></p>
    <p class="time">from 5pm</p>
  </section>

  <section class="toppings">
    <h2>Toppings</h2>
    <ul>
      <li>Philly Cheese Steak</li>
      <li>Cheese burger Smash</li>
      <li>Burnt End Beanz</li>
    </ul>
  </section>
</main>
</body>
</html>
```